Construction site banner with out Company information

I need a banner 4' tall and 6' wide, I want the banner to look very similar to the photo I uploaded from ChatGPT, make the person as life like as possible, I like the eyes to pop and be blue, and the hard hat orange, with the rest black and white, I have included our logo to use on the banner as well. Include the following:
Company Name: Rivlen Staffing
Temp Employees
General and Skilled Trades
Workers Comp and Payroll Coverage
www.rvlnstaff.com

Target Market(s)

Construction Companies

Requirements
Nice to have
• Realistic Person, bright blue eyes, orange hard hat
Should not have
• cartoon looking person

```html
<!DOCTYPE html>
<html lang="en">
<head>
<meta charset="utf-8">
<title>Rivlen Staffing – Site Banner</title>
<link href="https://fonts.googleapis.com/css2?family=Poppins:ital,wght@0,700;0,800;1,700;1,800&display=swap" rel="stylesheet">
<style>
  :root {
    --backdrop: #a9a9a9;
    --paper: #ffffff;
    --paper-shade: #ececec;
    --ink: #231f20;
    --orange: #ef5a24;
    --orange-light: #f7931e;
    --photo-dark: #3a3a3a;
    --photo-mid: #8d8d8d;
  }
  * { box-sizing: border-box; margin: 0; padding: 0; }
  html, body {
    width: 827px; height: 1200px; overflow: hidden;
    background: var(--backdrop);
    font-family: "Poppins", sans-serif;
  }
  .banner {
    position: absolute; left: 20px; top: 337px;
    width: 787px; height: 525px; overflow: hidden;
    background: repeating-linear-gradient(120deg, var(--paper) 0 60px, var(--paper-shade) 60px 62px, var(--paper) 62px 110px);
    box-shadow: 0 10px 24px rgba(0,0,0,.25);
  }
  .hero-photo {
    position: absolute; left: 240px; top: 0; width: 547px; height: 461px;
    clip-path: polygon(16% 0, 100% 0, 100% 100%, 38% 100%, 30% 30%, 0 14%);
    background:
      linear-gradient(180deg, var(--orange) 0 17%, transparent 17%),
      radial-gradient(ellipse at 65% 55%, var(--photo-mid), var(--photo-dark) 75%);
  }
  .brand { position: absolute; left: 54px; top: 48px; width: 186px; text-align: center; }
  .brand-name {
    font-weight: 800; font-size: 50px; line-height: 1; color: var(--orange);
    letter-spacing: -1px;
  }
  .brand-sub {
    margin-top: 18px; font-weight: 700; font-size: 19px; color: var(--ink); letter-spacing: .5px;
  }
  .services { position: absolute; left: 51px; top: 205px; list-style: none; }
  .service {
    position: relative; padding-left: 24px; margin-bottom: 12px;
    font-weight: 700; font-style: italic; font-size: 25px; line-height: 1.5; color: var(--ink);
  }
  .service::before {
    content: ""; position: absolute; left: 0; top: 13px;
    border-left: 10px solid var(--ink); border-top: 8px solid transparent; border-bottom: 8px solid transparent;
  }
  .accent { color: var(--orange); }
  .cta-bar { position: absolute; left: 0; bottom: 0; width: 787px; height: 64px; background: var(--ink); }
  .cta-apply {
    position: absolute; left: 60px; top: 0; line-height: 64px;
    font-weight: 800; font-style: italic; font-size: 31px; color: var(--paper);
  }
  .cta-web {
    position: absolute; left: 300px; top: 0; width: 487px; height: 64px;
    background: var(--orange); clip-path: polygon(0 0, 100% 0, 100% 100%, 5.3% 100%);
    padding-left: 40px; line-height: 64px;
    font-weight: 800; font-style: italic; font-size: 30px; color: var(--paper);
  }
</style>
</head>
<body>
  <section class="banner">
    <div class="hero-photo" role="img" aria-label="Black and white portrait of a bearded construction worker with bright blue eyes wearing an orange hard hat"></div>

    <div class="brand">
      <div class="brand-name">Rivlen</div>
      <div class="brand-sub">STAFFING</div>
    </div>

    <ul class="services">
      <li class="service"><span class="accent">Temp</span> Employees</li>
      <li class="service">General and<br><span class="accent">Skilled Trades</span></li>
      <li class="service">Workers Comp and<br><span class="accent">Payroll Coverage</span></li>
    </ul>

    <div class="cta-bar">
      <div class="cta-apply">APPLY NOW</div>
      <div class="cta-web">www.rvlnstaff.com</div>
    </div>
  </section>
</body>
</html>
```